Update New Business Card - For Start Up

I need to update my business card, I have our old version for example. I would like to keep to the same colors and theme. We are a threat reporting and case management tool for corporations and educational institutions.

Target Market(s)

Corporate Security and Human Resources, School Administrators and Superintendents.

Industry/Entity Type

Physical Security and Technology.

Contact Information for Business Card

My Name, Founder/CEO, phone number 555-214-6082, Logo, Web...

Colors
0054AA
0677BA
7BADD7
CADEEF
E8F1F8

Requirements
Must have
• Something new and trendy.

```html
<!DOCTYPE html>
<html lang="en">
<head>
<meta charset="utf-8">
<title>Vigilor Business Card</title>
<link rel="stylesheet" href="https://fonts.googleapis.com/css2?family=Montserrat:wght@500;700&family=Arimo:wght@400&display=swap">
<style>
  :root {
    --brand-blue: #1e74bb;
    --deep-blue: #0054aa;
    --white: #ffffff;
    --ink: #222222;
    --rule: #8a8a8a;
    --backdrop: #2b2b2b;
  }
  * { margin: 0; padding: 0; box-sizing: border-box; }
  html, body { width: 1200px; height: 1015px; overflow: hidden; }
  body {
    background: var(--backdrop);
    position: relative;
    font-family: "Arimo", Arial, sans-serif;
  }
  .card {
    position: absolute;
    left: 280px;
    width: 640px;
    height: 366px;
    overflow: hidden;
    box-shadow: 0 10px 30px rgba(0,0,0,0.5);
  }
  .card-front { top: 110px; background: var(--brand-blue); }
  .card-back { top: 540px; background: var(--white); }

  .brand-lockup {
    position: absolute;
    left: 170px;
    top: 152px;
    display: flex;
    align-items: center;
    gap: 18px;
  }
  .brand-dot {
    width: 58px; height: 58px;
    border-radius: 50%;
    background: var(--white);
  }
  .brand-name {
    font-family: "Montserrat", sans-serif;
    font-weight: 500;
    font-size: 44px;
    letter-spacing: 6px;
    color: var(--white);
  }

  .back-graphics { position: absolute; inset: 0; }

  .person {
    position: absolute;
    left: 130px;
    top: 262px;
    text-align: right;
    width: 230px;
  }
  .person-name {
    font-family: "Montserrat", sans-serif;
    font-weight: 700;
    font-size: 22px;
    letter-spacing: 3px;
    color: var(--brand-blue);
  }
  .person-title {
    font-family: "Montserrat", sans-serif;
    font-weight: 500;
    font-size: 17px;
    color: var(--ink);
    margin-top: 2px;
  }
  .divider {
    position: absolute;
    left: 380px;
    top: 250px;
    width: 1px;
    height: 80px;
    background: var(--rule);
  }
  .contact-list {
    position: absolute;
    left: 396px;
    top: 248px;
    list-style: none;
  }
  .contact-item {
    display: flex;
    align-items: center;
    gap: 10px;
    height: 28px;
    font-size: 15px;
    color: var(--ink);
  }
  .contact-icon { width: 22px; height: 22px; flex: none; }
</style>
</head>
<body>
  <section class="card card-front" aria-label="Card front">
    <div class="brand-lockup">
      <span class="brand-dot"></span>
      <span class="brand-name">VIGILOR</span>
    </div>
  </section>

  <section class="card card-back" aria-label="Card back">
    <svg class="back-graphics" width="640" height="366" viewBox="0 0 640 366" aria-hidden="true">
      <rect class="band-left" x="0" y="170" width="300" height="78" fill="var(--brand-blue)"/>
      <rect class="band-right" x="300" y="92" width="340" height="78" fill="var(--brand-blue)"/>
      <circle class="band-disc" cx="300" cy="170" r="96" fill="var(--brand-blue)" stroke="var(--white)" stroke-width="18"/>
    </svg>

    <div class="person">
      <div class="person-name">ADAM KESSLER</div>
      <div class="person-title">Founder / CEO</div>
    </div>

    <div class="divider"></div>

    <ul class="contact-list">
      <li class="contact-item">
        <svg class="contact-icon" viewBox="0 0 22 22" aria-hidden="true">
          <circle cx="11" cy="11" r="11" fill="var(--brand-blue)"/>
          <path d="M7.5 6 L9.5 6 L10.3 8.6 L9 9.6 Q10 12 12.4 13 L13.4 11.7 L16 12.5 L16 14.5 Q15.5 16 13.5 16 Q6 15 6 7.5 Q6 6 7.5 6 Z" fill="var(--white)"/>
        </svg>
        <span>555-214-6082</span>
      </li>
      <li class="contact-item">
        <svg class="contact-icon" viewBox="0 0 22 22" aria-hidden="true">
          <circle cx="11" cy="11" r="11" fill="var(--brand-blue)"/>
          <rect x="5.5" y="7" width="11" height="8" fill="var(--white)"/>
          <path d="M5.5 7 L11 11.5 L16.5 7" fill="none" stroke="var(--brand-blue)" stroke-width="1"/>
        </svg>
        <span>adam@vigilor.co</span>
      </li>
      <li class="contact-item">
        <svg class="contact-icon" viewBox="0 0 22 22" aria-hidden="true">
          <circle cx="11" cy="11" r="11" fill="var(--brand-blue)"/>
          <g fill="none" stroke="var(--white)" stroke-width="1">
            <circle cx="11" cy="11" r="5.5"/>
            <ellipse cx="11" cy="11" rx="2.4" ry="5.5"/>
            <line x1="5.5" y1="11" x2="16.5" y2="11"/>
            <line x1="6.3" y1="8.3" x2="15.7" y2="8.3"/>
            <line x1="6.3" y1="13.7" x2="15.7" y2="13.7"/>
          </g>
        </svg>
        <span>www.vigilor.co</span>
      </li>
    </ul>
  </section>
</body>
</html>
```